Harlow Crest Holdings (Remodeling company) needs a logo and business card

We need a business card design for a new company. We "flip" upmarket houses (buy, remodel and sell) in the Austin, TX area. I'd like neutral colors (grey, white, gold black). I would like it to include a simple, clean logo. Our designs are modern and uncluttered and I would like that reflected in the business card design.

Target Market(s)

Young professionals, Families, Retirees. Our properties will sell for $750k+

Industry/Entity Type

Real Estate

Contact Information for Business Card

Harlow Crets Holdings
Mona Harlow
(979) 555 0142
Owner
Rolf Tandem
(512) 555 0176
Realtor

Logo Text

Harlow Crest Holdings

Font styles to use
Serif
Script

Requirements
Must have
• Simple, classic design
Nice to have
• Clean lines, modern look
Should not have
• Too traditionally

```html
<!DOCTYPE html>
<html lang="en">
<head>
<meta charset="utf-8">
<title>Harlow Crest Holdings — Business Card</title>
<link rel="stylesheet" href="https://fonts.googleapis.com/css2?family=Lato:wght@300;400;700;900&display=swap">
<style>
  :root {
    --backdrop: #d8ccc5;
    --card: #ffffff;
    --brand-teal: #2fb3bd;
    --ink: #1f1f1f;
    --ink-soft: #333333;
  }
  html, body {
    margin: 0;
    padding: 0;
    width: 1200px;
    height: 800px;
    overflow: hidden;
    background: var(--backdrop);
    font-family: "Lato", Arial, sans-serif;
  }
  .canvas {
    position: relative;
    width: 1200px;
    height: 800px;
  }
  .business-card {
    position: absolute;
    left: 276px;
    top: 231px;
    width: 592px;
    height: 328px;
    background: var(--card);
    box-shadow: 0 2px 6px rgba(0,0,0,0.12);
  }
  .brand {
    position: absolute;
    left: 30px;
    top: 76px;
    width: 246px;
    text-align: center;
  }
  .brand-mark {
    display: block;
    width: 100px;
    height: 100px;
    margin: 0 auto 10px;
    border-radius: 50%;
    background: var(--brand-teal);
  }
  .brand-name {
    margin: 0;
    font-weight: 300;
    font-size: 27px;
    line-height: 1.05;
    color: var(--brand-teal);
  }
  .contacts {
    position: absolute;
    left: 338px;
    top: 58px;
  }
  .contact + .contact {
    margin-top: 40px;
  }
  .contact-name {
    margin: 0;
    font-weight: 900;
    font-size: 28px;
    line-height: 1;
    color: var(--ink);
    letter-spacing: -0.2px;
  }
  .contact-role {
    margin: 4px 0 0 2px;
    font-weight: 400;
    font-size: 19px;
    line-height: 1.2;
    color: var(--ink-soft);
  }
  .contact-phone {
    margin: 8px 0 0 2px;
    font-weight: 400;
    font-size: 16px;
    color: var(--ink-soft);
  }
</style>
</head>
<body>
  <main class="canvas">
    <section class="business-card">
      <div class="brand">
        <span class="brand-mark"></span>
        <p class="brand-name">Harlow Crest<br>Holdings</p>
      </div>
      <div class="contacts">
        <div class="contact">
          <h2 class="contact-name">Mona Harlow</h2>
          <p class="contact-role">OWNER</p>
          <p class="contact-phone">(979) 555 0142</p>
        </div>
        <div class="contact">
          <h2 class="contact-name">Rolf Tandem</h2>
          <p class="contact-role">REALTOR</p>
          <p class="contact-phone">(512) 555 0176</p>
        </div>
      </div>
    </section>
  </main>
</body>
</html>
```